Velmar Computers Brochure design

We need an brochure, in a4 size, it should be 8 pages in total.

We have 9 topics we need covered:
Front page
Velmar introduction
Velmar office series
Velmar Business series
Velmar Performance series
Partners
Oxbrin
Warranty
Contact details, Back page

WE have a new material we want to use instead of the current oxbrin page:

https://www.filecrate-example.com/s/qp7rmxwatg3kzn2/OXBRIN.pdf

• I have added a PowerPoint presentation with information we want in the brochure. There are 9 pages, so if you can merge two of them together to one so we get a total of 8 pages.

I have also added pictures of TQ screens, that can be bundled with all our machines. We also want that to be shown some where, maybe on same page as the computers.

```html
<!DOCTYPE html>
<html lang="en">
<head>
<meta charset="utf-8">
<title>Velmar Computers Brochure – Introduction Spread</title>
<link href="https://fonts.googleapis.com/css2?family=Roboto+Condensed:wght@400;700&display=swap" rel="stylesheet">
<style>
  :root {
    --canvas: #ffffff;
    --paper: #ffffff;
    --blue-deep: #0b63b4;
    --blue-mid: #1a7bc9;
    --blue-light: #4d9bd9;
    --glow: #8cc2ec;
    --ink: #07122a;
    --white: #ffffff;
    --photo-top: #c9d2db;
    --photo-bottom: #27345a;
    --mark: #333333;
  }
  * { box-sizing: border-box; margin: 0; padding: 0; }
  html, body { width: 1200px; height: 806px; overflow: hidden; background: var(--canvas); }
  body { position: relative; font-family: "Roboto Condensed", "Arial Narrow", sans-serif; }

  .crop-mark { position: absolute; left: 606px; width: 1px; height: 22px; background: var(--mark); }
  .crop-mark--top { top: 24px; }
  .crop-mark--bottom { top: 746px; }

  .spread {
    position: absolute; left: 126px; top: 54px; width: 960px; height: 680px;
    background: var(--paper);
    box-shadow: 0 0 10px rgba(0,0,0,0.18);
  }
  .spread__bleed {
    position: absolute; left: 34px; top: 0; width: 892px; height: 679px;
    background:
      radial-gradient(ellipse 340px 260px at 690px 320px, rgba(140,194,236,0.75) 0%, rgba(140,194,236,0.35) 55%, rgba(140,194,236,0) 100%),
      linear-gradient(180deg, var(--blue-deep) 0%, var(--blue-mid) 55%, var(--blue-light) 100%);
    overflow: hidden;
  }
  .spread__texture {
    position: absolute; inset: 0;
    background: linear-gradient(160deg, rgba(255,255,255,0.08) 0%, rgba(255,255,255,0) 40%, rgba(255,255,255,0.1) 75%, rgba(255,255,255,0) 100%);
  }

  .photo {
    position: absolute; left: 0; top: 162px; width: 446px; height: 277px;
    background: linear-gradient(160deg, var(--photo-top) 0%, #8e9bb0 45%, var(--photo-bottom) 100%);
  }
  .photo-caption {
    position: absolute; left: 34px; top: 444px; font-size: 8.4px; color: var(--ink);
  }

  .brand {
    position: absolute; left: 785px; top: 42px;
    font-weight: 700; font-size: 18px; letter-spacing: 0.3px; color: var(--white);
  }

  .intro {
    position: absolute; left: 548px; top: 162px; width: 274px;
    font-size: 8.3px; line-height: 15.6px; color: var(--ink);
  }
  .intro p + p { margin-top: 15px; }

  .page-number {
    position: absolute; left: 942px; top: 652px;
    font-size: 13px; font-weight: 700; color: var(--blue-mid); text-decoration: underline;
  }
</style>
</head>
<body>
  <div class="crop-mark crop-mark--top"></div>
  <div class="crop-mark crop-mark--bottom"></div>

  <section class="spread">
    <div class="spread__bleed">
      <div class="spread__texture" role="img" aria-label="Soft blue background with flowing line pattern"></div>

      <div class="photo" role="img" aria-label="Photograph of business people in suits working around a round table with a laptop, papers and coffee"></div>
      <p class="photo-caption">Velmar Computers is an official Oxbrin <sup>®</sup> Technology Provider Partner.</p>

      <div class="brand">VELMAR</div>

      <div class="intro">
        <p>”VELMAR” is a registered trademark by Velmar Computers Ltd. under which we began to assemble our own range of desktop computers in February 2013. At this point it had taken more than 2 years of planning to start up the project.</p>
        <p>All desktop computers are being produced at our premises in Dar es Salaam, Tanzania, where a combined team of skillful Tanzanian and Danish computer professionals are assembling the final VELMAR product. The VELMAR desktop assembly plant is partly financially supported by The Meridian Fund for Emerging Economies which is an independent investment fund owned by the Danish government.</p>
        <p>The Assembly ProcessDuring the assembly process, all parts are specifically selected and all serial numbers of all the components are tracked and stored in our database. That way we always know exactly which components are in which machine, when the system was assembled, when it was sold and to whom it was delivered.</p>
        <p>We have standardized procedures for the assembly processes ensuring that all parts are in the right place and connected properly to the right parts. All systems undergo a stress test followed by a manual physical inspection to make sure that the consumer will not end up with a faulty product.</p>
      </div>
    </div>
    <div class="page-number">1</div>
  </section>
</body>
</html>
```